Psychotherapist need a business card with logo

I am a psychotherapist in need of a business card. The card must have:

Marisol Trevuneda
Psicoterapeuta
937 281 706

Psychologists use the greek letter psy, which is the psychologist symbol, but I would prefer something like a mandala, a graphic symbol, an iconic tree, nothing very usual, but something that shows confidence and trust.

Industry/Entity Type

Business

```html
<!DOCTYPE html>
<html lang="es">
<head>
<meta charset="utf-8">
<title>Marisol Trevuneda — Psicoterapeuta</title>
<link rel="stylesheet" href="https://fonts.googleapis.com/css2?family=Allura&family=Questrial&display=swap">
<style>
  :root {
    --card-bg: #f7f7f6;
    --ink: #1c1c1c;
    --rule: #2a2a2a;
    --leaf-dark: #1f7a3c;
    --leaf-mid: #4f9a3f;
    --leaf-light: #8cc26a;
  }
  html, body {
    margin: 0;
    padding: 0;
    width: 1200px;
    height: 720px;
    overflow: hidden;
    background: var(--card-bg);
  }
  .card {
    position: relative;
    width: 1200px;
    height: 720px;
    background: var(--card-bg);
    color: var(--ink);
  }
  .card__emblem {
    position: absolute;
    left: 520px;
    top: 92px;
    width: 160px;
    height: 176px;
  }
  .card__name {
    position: absolute;
    left: 0;
    width: 1200px;
    top: 300px;
    margin: 0;
    text-align: center;
    font-family: "Allura", cursive;
    font-weight: 400;
    font-size: 62px;
    line-height: 1;
    color: var(--ink);
  }
  .card__rule {
    position: absolute;
    left: 275px;
    top: 420px;
    width: 650px;
    height: 0;
    border-top: 2px solid var(--rule);
  }
  .card__role {
    position: absolute;
    left: 0;
    width: 1200px;
    top: 446px;
    margin: 0;
    text-align: center;
    font-family: "Questrial", sans-serif;
    font-size: 28px;
    letter-spacing: 0.62em;
    text-indent: 0.62em;
    color: var(--ink);
  }
  .card__phone {
    position: absolute;
    left: 0;
    width: 1200px;
    top: 514px;
    margin: 0;
    text-align: center;
    font-family: "Questrial", sans-serif;
    font-size: 25px;
    letter-spacing: 0.14em;
    color: var(--ink);
  }
</style>
</head>
<body>
  <main class="card">
    <svg class="card__emblem" viewBox="0 0 160 176" role="img" aria-label="Emblema de árbol con copa redonda de hojas verdes">
      <defs>
        <radialGradient id="canopy" cx="45%" cy="40%" r="60%">
          <stop offset="0%" stop-color="var(--leaf-light)"/>
          <stop offset="55%" stop-color="var(--leaf-mid)"/>
          <stop offset="100%" stop-color="var(--leaf-dark)"/>
        </radialGradient>
      </defs>
      <circle cx="80" cy="80" r="78" fill="url(#canopy)"/>
    </svg>

    <h1 class="card__name">Marisol Trevuneda</h1>
    <div class="card__rule"></div>
    <p class="card__role">PSICOTERAPEUTA</p>
    <p class="card__phone">937 281 706</p>
  </main>
</body>
</html>
```